New modern website for Kerbline Groundworks

Hi we are an existing company that has a current website http://www.kerblinegroundworks.co.nz/ we are looking to get a new vibrant looking website designed to take us further and gain more customers. We are after a simple easy to use website that does not confuse but we want to make an impact and stand out from the rest

Target Market(s)

Homeowners And Commercial Businesses

Industry/Entity Type

It Company

Coding

Coded - Design and coding required

Number of Pages Required

2 page

```html
<!DOCTYPE html>
<html lang="en">
<head>
<meta charset="utf-8">
<title>Kerbline Groundworks</title>
<link href="https://fonts.googleapis.com/css2?family=Kanit:wght@400;500;600&family=Open+Sans:wght@400;600;700&display=swap" rel="stylesheet">
<style>
:root{
  --yellow:#dba51c;
  --yellow-deep:#c8910f;
  --ink:#1d1d1d;
  --text:#444;
  --dark:#2e3133;
  --footer:#2a2a2a;
  --footer-bar:#1c1c1c;
  --grey-box:#dedede;
  --white:#fff;
}
*{margin:0;padding:0;box-sizing:border-box}
html,body{width:1200px;height:3020px;overflow:hidden}
body{position:relative;background:var(--white);font-family:"Open Sans",sans-serif;color:var(--text)}
.abs{position:absolute}
.site-header{left:0;top:0;width:1200px;height:95px;background:var(--white);z-index:3}
.brand{left:66px;top:24px;display:flex;align-items:center;gap:12px;font-family:"Kanit",sans-serif;font-weight:600;font-size:28px;color:var(--ink);letter-spacing:.5px}
.brand-mark{width:16px;height:16px;background:var(--ink)}
.main-nav{left:470px;top:0;height:95px;display:flex}
.main-nav a{display:block;height:95px;line-height:95px;padding:0 14px;font-size:14px;font-weight:700;color:var(--ink);text-decoration:none;text-transform:uppercase}
.main-nav a.active{box-shadow:inset 0 -4px 0 var(--yellow)}
.header-phone{left:978px;top:36px;display:flex;align-items:center;gap:10px;font-size:20px;color:var(--ink)}
.hero{left:0;top:95px;width:1200px;height:529px;background:linear-gradient(160deg,#6b5e52 0%,#3b3834 45%,#262524 100%)}
.hero-title{left:0;top:236px;width:1200px;text-align:center;font-family:"Kanit",sans-serif;font-weight:500;font-size:46px;color:var(--white)}
.hero-sub{left:0;top:310px;width:1200px;text-align:center;font-family:"Kanit",sans-serif;font-weight:400;font-size:40px;color:var(--white)}
.hero-rule{left:340px;top:372px;width:472px;height:2px;background:var(--yellow)}
.promo-card{top:535px;width:510px;height:258px;border:4px solid var(--white);box-shadow:0 6px 14px rgba(0,0,0,.25);background:linear-gradient(135deg,#e2b12a,#d29c12);text-align:center;color:var(--ink);z-index:2}
.promo-card h2{margin-top:50px;font-family:"Kanit",sans-serif;font-weight:600;font-size:42px;line-height:1.1}
.promo-card p{margin-top:20px;font-size:17px;font-weight:600;text-transform:uppercase}
.promo-card .more{display:inline-block;margin-top:24px;padding-bottom:8px;border-bottom:2px solid var(--ink);font-size:15px;font-weight:700;color:var(--ink);text-decoration:none}
.who-heading{left:66px;top:900px;font-family:"Kanit",sans-serif;font-weight:600;font-size:40px;color:var(--ink)}
.who-rule{left:66px;top:960px;width:114px;height:4px;background:var(--yellow)}
.who-text{left:66px;top:985px;width:400px;font-size:14px;line-height:21px;color:var(--text)}
.btn-outline{left:66px;top:1121px;width:147px;height:40px;border:1px solid #999;font-size:13px;font-weight:700;color:var(--ink);text-align:center;line-height:38px;text-decoration:none}
.team-photo{left:554px;top:902px;width:543px;height:350px;background:linear-gradient(180deg,#e9eef3,#8e97a3 55%,#5b6577)}
.trust{left:0;top:1252px;width:1200px;height:546px;background:linear-gradient(180deg,#3a3d40,#26292b)}
.trust-title{left:0;top:1296px;width:1200px;text-align:center;font-family:"Kanit",sans-serif;font-weight:500;font-size:26px;color:var(--white)}
.feature{top:1385px;width:340px;text-align:center;color:var(--white)}
.feature-icon{display:block;width:164px;height:164px;margin:0 auto;border-radius:50%}
.feature-icon.solid{background:var(--yellow)}
.feature svg{display:block;margin:0 auto}
.feature .bar{width:130px;height:2px;background:var(--yellow);margin:33px auto 0}
.feature h3{margin-top:8px;font-family:"Kanit",sans-serif;font-weight:500;font-size:22px}
.feature p{margin-top:12px;font-size:14px;line-height:21px;color:#e7e7e7}
.ask-box{left:66px;top:1866px;width:669px;height:133px;background:var(--grey-box)}
.ask-text{left:84px;top:1872px;width:520px;font-family:"Kanit",sans-serif;font-weight:500;font-size:34px;line-height:56px;color:var(--ink)}
.ask-text span{color:var(--yellow)}
.contact-lines{left:783px;top:1888px;font-size:26px;line-height:44px;color:var(--ink)}
.contact-lines b{font-weight:400;color:var(--yellow);display:inline-block;width:96px}
.gallery-band{left:0;top:2106px;width:1200px;height:598px;background:linear-gradient(180deg,#d29c14,#bf8a10)}
.gallery-title{left:0;top:2152px;width:1200px;text-align:center;font-family:"Kanit",sans-serif;font-weight:500;font-size:30px;color:var(--ink)}
.shot{background:linear-gradient(160deg,#8a8f94,#3a3d40)}
.zoom{left:398px;top:2404px;width:56px;height:56px}
.site-footer{left:0;top:2704px;width:1200px;height:292px;background:var(--footer)}
.foot-head{top:2744px;font-size:15px;font-weight:700;color:var(--white);text-transform:uppercase;letter-spacing:.5px;padding-bottom:8px;border-bottom:2px solid var(--yellow)}
.foot-brand{left:99px;top:2790px;font-family:"Kanit",sans-serif;font-weight:600;font-size:24px;color:var(--white)}
.foot-about{left:99px;top:2842px;width:320px;font-size:12px;line-height:18px;color:#888}
.socials{left:99px;top:2926px;display:flex;gap:14px}
.socials i{display:block;width:11px;height:11px;border-radius:50%;background:#bbb}
.foot-links{top:2800px;list-style:none;font-size:12px;line-height:31px;color:#bbb}
.foot-links li::before{content:"›";color:#777;margin-right:10px}
.office{left:829px;top:2800px;list-style:none;font-size:12px;line-height:31px;color:#999}
.office li{display:flex;align-items:center;gap:14px}
.office svg{flex:none}
.copyright{left:0;top:2996px;width:1200px;height:24px;background:var(--footer-bar);font-size:11px;line-height:24px;text-align:center;color:#999}
</style>
</head>
<body>

<header class="site-header abs">
  <div class="brand abs"><span class="brand-mark"></span>KERBLINE GROUNDWORKS</div>
  <nav class="main-nav abs">
    <a class="active" href="#">Home</a><a href="#">About</a><a href="#">Services</a><a href="#">Projects</a><a href="#">Contact Us</a>
  </nav>
  <div class="header-phone abs">
    <svg width="24" height="24" viewBox="0 0 24 24"><path d="M6.6 10.8a15 15 0 0 0 6.6 6.6l2.2-2.2a1 1 0 0 1 1-.25 11.4 11.4 0 0 0 3.6.6 1 1 0 0 1 1 1V20a1 1 0 0 1-1 1A17 17 0 0 1 3 4a1 1 0 0 1 1-1h3.5a1 1 0 0 1 1 1c0 1.25.2 2.45.6 3.6a1 1 0 0 1-.25 1z" fill="#dba51c"/></svg>
    09 555 0142
  </div>
</header>

<section class="hero abs" role="img" aria-label="Road crew spreading fresh asphalt with rakes"></section>
<h1 class="hero-title abs">Your one-stop specialist for driveway</h1>
<p class="hero-sub abs">construction in Auckland</p>
<div class="hero-rule abs"></div>

<article class="promo-card abs" style="left:66px">
  <h2>Our Services</h2>
  <p>Complete asphalt services for your next</p>
  <a class="more" href="#">READ MORE</a>
</article>
<article class="promo-card abs" style="left:626px">
  <h2>Project</h2>
  <p>For residential driveways and commercial</p>
  <a class="more" href="#">READ MORE</a>
</article>

<h2 class="who-heading abs">WHO WE ARE</h2>
<div class="who-rule abs"></div>
<p class="who-text abs">Embedded in our culture of hard work, honesty, and getting the well done job, our history tells not only much about our past but also it does our present. Our record of succeeding, surviving, and striving to be the best is central to our reputation today.</p>
<a class="btn-outline abs" href="#">READ MORE</a>
<div class="team-photo abs" role="img" aria-label="Group of construction workers in hard hats and overalls"></div>

<section class="trust abs" role="img" aria-label="Dark asphalt surface background"></section>
<h2 class="trust-title abs">The trusted name for all Concrete &amp; Asphalt Paving in Auckland</h2>

<div class="feature abs" style="left:61px">
  <div class="feature-icon solid" role="img" aria-label="Years of experience badge"></div>
  <div class="bar"></div>
  <h3>OUR EXPERTISE</h3>
  <p>We have a reputation with clients in and around Auckland for achieving great results on time and within budget every time. We are proud to share our years of experience.</p>
</div>
<div class="feature abs" style="left:428px">
  <svg width="164" height="164" viewBox="0 0 164 164">
    <circle cx="82" cy="82" r="74" fill="none" stroke="#dba51c" stroke-width="8"/>
    <path d="M82 40 L124 76 H112 V112 H52 V76 H40 Z" fill="#dba51c"/>
    <rect x="74" y="88" width="16" height="24" fill="#2e3133"/>
  </svg>
  <div class="bar"></div>
  <h3>CONCRETING &amp; WORK</h3>
  <p>When it comes to all asphalt services, you can rest assured we will work around your schedule, requirements and budget. Servicing throughout Auckland, we specialise in.</p>
</div>
<div class="feature abs" style="left:798px">
  <div class="feature-icon solid" role="img" aria-label="Worker digging roadworks icon"></div>
  <div class="bar"></div>
  <h3>ADDITIONAL SERVICES</h3>
  <p>As part of our asphalt services, we are proud to offer a range of related services to our clients in the eastern suburbs and greater Auckland. Specialising in residential, commercial and industrial projects.</p>
</div>

<div class="ask-box abs"></div>
<svg class="abs" style="left:735px;top:1916px" width="18" height="34" viewBox="0 0 18 34"><path d="M0 0 L18 17 L0 34 Z" fill="#dedede"/></svg>
<p class="ask-text abs">Any Questions you would like to ask? <span>Need to talk to us...</span></p>
<svg class="abs" style="left:624px;top:1892px" width="84" height="84" viewBox="0 0 24 24"><path d="M6.6 10.8a15 15 0 0 0 6.6 6.6l2.2-2.2a1 1 0 0 1 1-.25 11.4 11.4 0 0 0 3.6.6 1 1 0 0 1 1 1V20a1 1 0 0 1-1 1A17 17 0 0 1 3 4a1 1 0 0 1 1-1h3.5a1 1 0 0 1 1 1c0 1.25.2 2.45.6 3.6a1 1 0 0 1-.25 1z" fill="#1d1d1d"/><path d="M14.5 3.5a6.5 6.5 0 0 1 6 6M14 6.6a3.5 3.5 0 0 1 3.4 3.4" fill="none" stroke="#1d1d1d" stroke-width="1.4" stroke-linecap="round"/></svg>
<div class="contact-lines abs">
  <div><b>Mobile:</b>027 555 0178</div>
  <div><b>Phone:</b>&nbsp;09 555 0142</div>
</div>

<section class="gallery-band abs" role="img" aria-label="Road surface with yellow tint"></section>
<h2 class="gallery-title abs">For residential driveways and commercial paving in Auckland</h2>
<div class="shot abs" style="left:74px;top:2275px;width:170px;height:145px" role="img" aria-label="Traffic cones beside new asphalt"></div>
<div class="shot abs" style="left:74px;top:2444px;width:170px;height:145px" role="img" aria-label="Asphalt path beside a wall"></div>
<div class="shot abs" style="left:262px;top:2275px;width:328px;height:316px;background:linear-gradient(160deg,#6d7076,#34373a)" role="img" aria-label="Crew laying asphalt on a site"></div>
<svg class="zoom abs" viewBox="0 0 56 56"><circle cx="28" cy="28" r="28" fill="rgba(255,255,255,.6)"/><circle cx="25" cy="25" r="9" fill="none" stroke="#333" stroke-width="3"/><path d="M32 32 L40 40" stroke="#333" stroke-width="3" stroke-linecap="round"/><path d="M21 25h8M25 21v8" stroke="#333" stroke-width="2"/></svg>
<div class="shot abs" style="left:608px;top:2275px;width:316px;height:316px;background:linear-gradient(180deg,#c9d4de 0%,#b54848 45%,#7b7f83 70%,#55585b)" role="img" aria-label="Fleet of red trucks parked in a row"></div>
<div class="shot abs" style="left:942px;top:2275px;width:169px;height:145px" role="img" aria-label="Sealed driveway along a hedge"></div>
<div class="shot abs" style="left:942px;top:2444px;width:169px;height:145px;background:linear-gradient(160deg,#5a5d60,#1f2123)" role="img" aria-label="Fresh asphalt driveway"></div>

<footer class="site-footer abs"></footer>
<h4 class="foot-head abs" style="left:99px">About Us</h4>
<div class="foot-brand abs">KERBLINE GROUNDWORKS</div>
<p class="foot-about abs">Kerbline works as an established groundworks services company and is a leading builder in diverse and numerous market segments.</p>
<div class="socials abs"><i></i><i></i><i></i><i></i><i></i><i></i><i></i></div>

<h4 class="foot-head abs" style="left:465px">Information</h4>
<ul class="foot-links abs" style="left:465px"><li>Home</li><li>Projects</li><li>Certifications</li><li>Core Values</li><li>Our Partners</li></ul>
<ul class="foot-links abs" style="left:625px"><li>Company</li><li>Contact</li><li>Company History</li><li>FAQ</li><li>Our Team</li></ul>

<h4 class="foot-head abs" style="left:829px">Structure Office</h4>
<ul class="office abs">
  <li><svg width="12" height="14" viewBox="0 0 12 14"><path d="M6 0a5 5 0 0 1 5 5c0 4-5 9-5 9S1 9 1 5a5 5 0 0 1 5-5z" fill="#888"/><circle cx="6" cy="5" r="2" fill="#2a2a2a"/></svg>22 Harbour Lane, Auckland.</li>
  <li><svg width="12" height="12" viewBox="0 0 24 24"><path d="M6.6 10.8a15 15 0 0 0 6.6 6.6l2.2-2.2a1 1 0 0 1 1-.25 11.4 11.4 0 0 0 3.6.6 1 1 0 0 1 1 1V20a1 1 0 0 1-1 1A17 17 0 0 1 3 4a1 1 0 0 1 1-1h3.5a1 1 0 0 1 1 1c0 1.25.2 2.45.6 3.6a1 1 0 0 1-.25 1z" fill="#888"/></svg>(09) 555 0190</li>
  <li><svg width="13" height="10" viewBox="0 0 13 10"><rect width="13" height="10" fill="#888"/><path d="M0 0 L6.5 5.5 L13 0" fill="none" stroke="#2a2a2a" stroke-width="1.2"/></svg>info@kerblinegroundworks.co.nz</li>
  <li><svg width="13" height="12" viewBox="0 0 13 12"><rect y="3" width="13" height="9" fill="#888"/><rect x="3" width="7" height="4" fill="#888"/></svg>(09) 555 0191</li>
  <li><svg width="13" height="13" viewBox="0 0 13 13"><circle cx="6.5" cy="6.5" r="5.5" fill="none" stroke="#888" stroke-width="1.4"/><path d="M6.5 3v3.5h2.5" fill="none" stroke="#888" stroke-width="1.4"/></svg>Mon - Sat: 9:00 - 18:00</li>
</ul>

<div class="copyright abs">Copyright © 2016 Kerbline Groundworks - All Rights Reserved.</div>

</body>
</html>
```